Wine Label - Design required by La Brisuela

2 Independent chilean winemakers here!
La Brisuela (means door slam or slam), that is the brand for our wines (2 wines at the moment), low scale production.
We would like to have front label for our wine out of the mainstream typical french classic style. Some words to describe it: youthful yet vintage/ Tobiah Vance/ pellman/ comic/ old western. Something i would wear on a t-shirt.
The text that is has to be on the label:
- La Brisuela (the brand)
-Field Blend (the type of one of the wines we have)
- 2018
- Wine of Chile.
It goes on sloping shoulder bottle, Burgundy model.
It is meant to cover a space of 3 1/4 h x 4 1/2 w inches . (or 8,5 cm height x 11cm width).
We like colours so...be creative!
I have attached the "La Brisuela" logo. We can changed it of course.
Thanks !

Target Market(s)

young drinkers (legally allowed to drink!)

Font styles to use
Other font styles liked:
• stencil

Colors

Designer to choose colors to be used in the design.

Requirements
Should not have
• Obvious wine things like glasses of wine, vines, grapes etc.

```html
<!DOCTYPE html>
<html lang="en">
<head>
<meta charset="utf-8">
<title>La Brisuela — Field Blend 2018 Label</title>
<link rel="stylesheet" href="https://fonts.googleapis.com/css2?family=Oswald:wght@500&family=Courier+Prime:wght@400;700&display=swap">
<style>
  :root {
    --backdrop: #dedede;
    --label-red: #ef2630;
    --burst-yellow: #f4ea1e;
    --ink: #1b1514;
  }
  html, body {
    margin: 0;
    padding: 0;
    width: 1136px;
    height: 1200px;
    overflow: hidden;
    background: var(--backdrop);
  }
  .canvas {
    position: relative;
    width: 1136px;
    height: 1200px;
    display: flex;
    align-items: center;
    justify-content: center;
  }
  .label {
    position: relative;
    width: 880px;
    height: 680px;
    background: var(--label-red);
    box-sizing: border-box;
    color: var(--ink);
  }
  .label__artwork {
    position: absolute;
    left: 230px;
    top: 30px;
    width: 420px;
    height: 330px;
    background: radial-gradient(ellipse at center, var(--burst-yellow) 0 45%, var(--label-red) 72%);
  }
  .label__note {
    position: absolute;
    top: 292px;
    margin: 0;
    font-family: "Courier Prime", monospace;
    font-size: 15px;
    line-height: 1.15;
  }
  .label__note--left { left: 100px; }
  .label__note--right { left: 680px; }
  .label__brand {
    position: absolute;
    left: 0;
    right: 0;
    top: 380px;
    margin: 0;
    text-align: center;
    font-family: "Oswald", sans-serif;
    font-weight: 500;
    font-size: 84px;
    letter-spacing: 4px;
    line-height: 1;
    color: var(--ink);
  }
  .label__specs {
    position: absolute;
    left: 100px;
    right: 100px;
    top: 496px;
    display: flex;
    align-items: center;
    justify-content: space-between;
    font-family: "Courier Prime", monospace;
    font-weight: 700;
    font-size: 15px;
  }
  .label__variety {
    display: flex;
    align-items: center;
    gap: 22px;
    font-family: "Oswald", sans-serif;
    font-weight: 500;
    font-size: 40px;
    letter-spacing: 1px;
  }
  .label__variety::before,
  .label__variety::after {
    content: "";
    width: 3px;
    height: 38px;
    background: var(--ink);
  }
  .label__rule {
    position: absolute;
    left: 100px;
    right: 100px;
    top: 562px;
    height: 4px;
    background: var(--ink);
  }
  .label__vintage {
    position: absolute;
    left: 0;
    right: 0;
    top: 578px;
    text-align: center;
    font-family: "Courier Prime", monospace;
    font-weight: 700;
    font-size: 34px;
    letter-spacing: 10px;
  }
</style>
</head>
<body>
  <main class="canvas">
    <section class="label">
      <div class="label__artwork" role="img" aria-label="Hand-drawn black double door in a yellow frame bursting from a yellow comic starburst, with 2018 above the door"></div>
      <p class="label__note label__note--left">Independent<br>winemakers</p>
      <p class="label__note label__note--right">Wine<br>of Chile</p>
      <h1 class="label__brand">LA BRISUELA</h1>
      <div class="label__specs">
        <span class="label__volume">750 ML</span>
        <span class="label__variety">FIELD BLEND</span>
        <span class="label__abv">13% VOL</span>
      </div>
      <div class="label__rule"></div>
      <div class="label__vintage">2018</div>
    </section>
  </main>
</body>
</html>
```